Business Card design for an International Import Export House

We need a Business Card design for our import export business. We trade in Minerals, Metals, Rice, Sugar, Steel etc.. The design should be minimalistic. It may or may not contain the physical address. In case you want to include the physical address - 418 Verandah Heights, Marlow Sector 9, Gurgaon, Haryana, India, 122009.

Target Market(s)

Steel Mills or Steel Plants, Factories, Mining businesses, Industrial houses, Government Agencies

Industry/Entity Type

Importer

Contact Information for Business Card

Business Name - Veloran Overseas

Font styles to use
Other font styles liked:
• montserrat

Requirements
Must have
• Ravi Kandola - President
• www.veloranoverseas.com
• ravi@veloranoverseas.com
• +91-987-654-3217
Nice to have
• worldwide suppliers of ores

```html
<!DOCTYPE html>
<html lang="en">
<head>
<meta charset="utf-8">
<title>Veloran Overseas – Business Card</title>
<link rel="stylesheet" href="https://fonts.googleapis.com/css2?family=Montserrat:wght@700;800&family=PT+Serif&display=swap">
<style>
  :root {
    --teal: #3a93a9;
    --charcoal: #3b3b3d;
    --ink: #232325;
    --paper: #ffffff;
    --stage: #e8e7e4;
    --contact-text: #f1f1f1;
  }
  * { box-sizing: border-box; margin: 0; padding: 0; }
  html, body {
    width: 1200px;
    height: 918px;
    overflow: hidden;
    background: var(--stage);
  }
  .card {
    position: absolute;
    left: 250px;
    width: 700px;
    height: 400px;
    background: var(--paper);
    overflow: hidden;
    box-shadow: 0 2px 10px rgba(0,0,0,0.08);
  }
  .card--front { top: 31px; }
  .card--back  { top: 487px; }

  /* Front */
  .brand {
    position: absolute;
    left: 0; right: 0; top: 110px;
    display: flex;
    flex-direction: column;
    align-items: center;
    gap: 18px;
  }
  .brand__dot {
    width: 74px; height: 74px;
    border-radius: 50%;
    background: var(--teal);
  }
  .brand__name {
    font-family: "Montserrat", sans-serif;
    font-weight: 800;
    font-size: 34px;
    letter-spacing: 0.5px;
    color: var(--teal);
    text-transform: uppercase;
    white-space: nowrap;
  }
  .tagline-band {
    position: absolute;
    left: 0; right: 0; top: 318px;
    height: 46px;
    background: var(--teal);
    display: flex;
    align-items: center;
    padding-left: 40px;
  }
  .tagline {
    font-family: "Montserrat", sans-serif;
    font-weight: 800;
    font-size: 22px;
    color: var(--ink);
    text-transform: uppercase;
  }

  /* Back */
  .holder {
    position: absolute;
    right: 22px; top: 162px;
    text-align: right;
    font-family: "Montserrat", sans-serif;
    text-transform: uppercase;
  }
  .holder__name { font-weight: 800; font-size: 24px; color: var(--teal); line-height: 1.05; }
  .holder__role { font-weight: 800; font-size: 15px; color: var(--ink); }

  .side-panel {
    position: absolute;
    left: 0; top: 200px;
    width: 62px; height: 150px;
    background: var(--teal);
  }
  .logo-box {
    position: absolute;
    left: 16px; top: 212px;
    width: 92px; height: 120px;
    background: var(--paper);
    border: 4px solid var(--teal);
    display: flex;
    flex-direction: column;
    align-items: center;
    justify-content: center;
    gap: 8px;
    z-index: 2;
  }
  .logo-box__dot { width: 34px; height: 34px; border-radius: 50%; background: var(--teal); }
  .logo-box__name {
    font-family: "Montserrat", sans-serif;
    font-weight: 800;
    font-size: 10.5px;
    line-height: 1.15;
    color: var(--teal);
    text-align: center;
    text-transform: uppercase;
  }
  .contact-band {
    position: absolute;
    left: 96px; right: 0; top: 222px;
    height: 112px;
    background: var(--charcoal);
    padding: 12px 0 0 34px;
  }
  .contact-list { list-style: none; }
  .contact-list li {
    display: flex;
    align-items: center;
    gap: 14px;
    height: 24px;
    font-family: "PT Serif", serif;
    font-size: 15px;
    color: var(--contact-text);
    white-space: nowrap;
  }
  .contact-list svg { width: 14px; height: 14px; flex: none; fill: var(--contact-text); }
  .base-band {
    position: absolute;
    left: 0; right: 0; top: 344px;
    height: 28px;
    background: var(--teal);
  }
</style>
</head>
<body>

<section class="card card--front" aria-label="Card front">
  <div class="brand">
    <span class="brand__dot"></span>
    <span class="brand__name">Veloran Overseas</span>
  </div>
  <div class="tagline-band">
    <span class="tagline">Worldwide Suppliers of Ores</span>
  </div>
</section>

<section class="card card--back" aria-label="Card back">
  <div class="holder">
    <div class="holder__name">Ravi Kandola</div>
    <div class="holder__role">President</div>
  </div>

  <div class="side-panel"></div>
  <div class="logo-box">
    <span class="logo-box__dot"></span>
    <span class="logo-box__name">Veloran<br>Overseas</span>
  </div>

  <div class="contact-band">
    <ul class="contact-list">
      <li>
        <svg viewBox="0 0 16 16" aria-hidden="true"><path d="M8 0a5.5 5.5 0 0 0-5.5 5.5C2.5 9.6 8 16 8 16s5.5-6.4 5.5-10.5A5.5 5.5 0 0 0 8 0zm0 8a2.5 2.5 0 1 1 0-5 2.5 2.5 0 0 1 0 5z"/></svg>
        418 Verandah Heights, Marlow Sector 9, Gurgaon, Haryana, India
      </li>
      <li>
        <svg viewBox="0 0 16 16" aria-hidden="true"><path d="M3.6 1l2.3 3.1-1.4 1.7c.9 2 2.6 3.7 4.7 4.7l1.7-1.4L14 11.4 12.4 14C6.6 13.6 2.4 9.4 2 3.6z"/></svg>
        +91-987-654-3217
      </li>
      <li>
        <svg viewBox="0 0 16 16" aria-hidden="true"><path d="M1 3h14v10H1zm1.4 1.2L8 8.6l5.6-4.4z"/></svg>
        ravi@veloranoverseas.com
      </li>
      <li>
        <svg viewBox="0 0 16 16" aria-hidden="true"><path d="M8 1a7 7 0 1 0 0 14A7 7 0 0 0 8 1zm4.9 6h-2.4a11 11 0 0 0-1-4.2A5.5 5.5 0 0 1 12.9 7zM8 2.6c.6.9 1.3 2.4 1.4 4.4H6.6C6.7 5 7.4 3.5 8 2.6zM6.5 2.8A11 11 0 0 0 5.5 7H3.1a5.5 5.5 0 0 1 3.4-4.2zM3.1 9h2.4a11 11 0 0 0 1 4.2A5.5 5.5 0 0 1 3.1 9zM8 13.4c-.6-.9-1.3-2.4-1.4-4.4h2.8c-.1 2-.8 3.5-1.4 4.4zm1.5-.2a11 11 0 0 0 1-4.2h2.4a5.5 5.5 0 0 1-3.4 4.2z"/></svg>
        www.veloranoverseas.com
      </li>
    </ul>
  </div>

  <div class="base-band"></div>
</section>

</body>
</html>
```